Club Membership Invitation

I am wanting to create a membership flyer/rackcard/postcard that schools can send back to me.
It is to promote ICT professional development for teachers and membership to "the club" will entitle the schools to special discounts of Professional Development rates, priority seating at workshops, the opportunity to join other schools in quality ICT  professional development.
Membership is free but they will need to send the form back to get membership.
Our website is www.crossingtheriver.example. which gives a flavour/ colours of our business

Updates
Hi, Could the name please be changed to The Lantern PD Club".
Thank you for the designs.

Target Market(s)
Primary Schools, Teachers, Leadership teams
Industry/Entity Type
Business
Requirements
Must have
- I would like it to be 2 sides.
Logo
"Lighting the Path PD Club"
Free membership
www.crossingtheriver.example
0508 ICT TUTOR
Benefits of membership...
Ongoing discounts
ICT PD clustering
Termly Specials
Priority seating at workshops
Early Bird notification
The form needs the address as it will beed to be sent or handed to...
ICT PD Membership
Lighting the Path
7 Kowhaiwai Terrace
Kelmore, 4736

```html
<!DOCTYPE html>
<html lang="en">
<head>
<meta charset="utf-8">
<title>Lighting the Path PD Club – Membership Rack Card</title>
<link href="https://fonts.googleapis.com/css2?family=Bubblegum+Sans&family=Roboto+Condensed:ital,wght@0,300;0,400;0,700;1,300&display=swap" rel="stylesheet">
<style>
  :root {
    --card-bg: #dceaf6;
    --page-bg: #ffffff;
    --brand-blue: #2a6cb4;
    --brand-red: #d3202e;
    --brand-orange: #e8873a;
    --ink: #1d1d1d;
    --muted: #9a9a9a;
    --panel: #ffffff;
    --grass-top: #9ccf4a;
    --grass-bottom: #4f8a1e;
  }
  * { box-sizing: border-box; margin: 0; padding: 0; }
  html, body { width: 1200px; height: 900px; overflow: hidden; }
  body { background: var(--page-bg); font-family: "Roboto Condensed", "Arial Narrow", sans-serif; color: var(--ink); position: relative; }

  .card {
    position: absolute; top: 0; width: 433px; height: 900px;
    background: var(--card-bg);
    box-shadow: 4px 4px 12px rgba(0,0,0,0.18);
    overflow: hidden;
  }
  .card--front { left: 147px; }
  .card--back { left: 621px; }

  .brand-mark {
    position: absolute; left: 0; right: 0;
    display: flex; align-items: center; justify-content: center; gap: 12px;
  }
  .brand-mark__dot { width: 22px; height: 22px; border-radius: 50%; background: var(--brand-orange); flex: none; }
  .brand-mark__name {
    font-family: "Bubblegum Sans", "Comic Sans MS", cursive;
    font-size: 44px; line-height: 1; color: var(--brand-blue); text-align: center;
  }
  .card--front .brand-mark { top: 100px; }
  .card--back .brand-mark { top: 95px; }

  .tagline {
    position: absolute; left: 0; right: 0; text-align: center;
    font-family: "Bubblegum Sans", "Comic Sans MS", cursive;
    color: var(--brand-blue); font-size: 29px; line-height: 1;
  }

  .club-title {
    position: absolute; top: 256px; left: 0; right: 0; text-align: center;
    font-style: italic; font-weight: 300; font-size: 32px; line-height: 1;
  }
  .card--front .tagline { top: 302px; }

  .offer-free {
    position: absolute; top: 340px; left: 0; right: 0; text-align: center;
    font-weight: 700; font-size: 158px; line-height: 1; color: var(--brand-red);
    letter-spacing: -2px;
  }
  .offer-membership {
    position: absolute; top: 476px; left: 0; right: 0; text-align: center;
    font-weight: 700; font-size: 54px; line-height: 1; color: var(--brand-red);
  }

  .benefits {
    position: absolute; left: 41px; top: 540px; width: 352px; height: 188px;
    background: var(--panel); box-shadow: 3px 3px 6px rgba(0,0,0,0.2);
    padding: 14px 0 0 52px;
  }
  .benefits__heading {
    font-family: "Bubblegum Sans", "Comic Sans MS", cursive;
    color: var(--brand-red); font-size: 29px; line-height: 1; margin: 0 0 6px -18px;
  }
  .benefits__list { list-style: none; }
  .benefits__list li { font-size: 20px; line-height: 25.5px; position: relative; padding-left: 25px; }
  .benefits__list li::before {
    content: ""; position: absolute; left: 0; top: 10px; width: 6px; height: 6px; background: var(--ink);
  }

  .contact { position: absolute; top: 746px; left: 0; right: 0; text-align: center; font-weight: 700; }
  .contact__intro { font-size: 19.5px; line-height: 26px; }
  .contact__web { font-size: 23px; line-height: 30px; }
  .contact__call { font-size: 19.5px; line-height: 26px; }
  .contact__phone { color: var(--brand-red); font-size: 23px; }

  .grass {
    position: absolute; left: 0; right: 0; bottom: 0; height: 76px;
    background: linear-gradient(180deg, var(--grass-top), var(--grass-bottom));
  }

  .card--back .tagline { top: 214px; }

  .form-panel {
    position: absolute; left: 20px; top: 256px; width: 395px; height: 512px;
    background: var(--panel); padding: 16px 21px 0 20px;
  }
  .form-panel__intro { font-weight: 700; font-size: 18px; line-height: 25px; margin-bottom: 14px; }
  .form-panel__intro em { font-style: normal; color: var(--brand-red); }
  .field { display: flex; align-items: flex-end; height: 39.6px; font-size: 14.5px; font-weight: 300; gap: 4px; }
  .field__line { flex: 1; border-bottom: 1.5px dotted #555; margin-bottom: 4px; }
  .field__label { white-space: nowrap; }
  .field--split .field__line--short { flex: 0 0 80px; }
  .field__gap { width: 4px; }
  .checkbox { display: inline-block; width: 10px; height: 10px; border: 1px solid var(--ink); margin: 0 4px 0 0; vertical-align: -1px; }
  .field__spacer { flex: 1; }
  .placeholder { color: var(--muted); }

  .return-box {
    position: absolute; left: 30px; top: 780px; width: 375px; height: 91px;
    border: 1px solid #333; text-align: center; padding-top: 8px;
  }
  .return-box__title { font-size: 21px; line-height: 25px; font-weight: 400; }
  .return-box__address { font-size: 18.5px; line-height: 24px; font-weight: 700; }
</style>
</head>
<body>

  <section class="card card--front" aria-label="Front of card">
    <div class="brand-mark"><span class="brand-mark__dot"></span><span class="brand-mark__name">Lighting<br>the Path</span></div>
    <h1 class="club-title">"Lighting the Path PD Club"</h1>
    <p class="tagline">Computer Training for Educators</p>
    <p class="offer-free">FREE</p>
    <p class="offer-membership">MEMBERSHIP</p>

    <div class="benefits">
      <h2 class="benefits__heading">Benefits of membership ...</h2>
      <ul class="benefits__list">
        <li>Ongoing discounts</li>
        <li>ICT PD clustering</li>
        <li>Termly Specials</li>
        <li>Priority seating at workshops</li>
        <li>Early Bird notification</li>
      </ul>
    </div>

    <div class="contact">
      <p class="contact__intro">For more information, please visit our website</p>
      <p class="contact__web">www.crossingtheriver.example</p>
      <p class="contact__call">or call us now <span class="contact__phone">0508 ICT TUTOR</span></p>
    </div>

    <div class="grass" role="img" aria-label="Strip of green grass along the bottom edge"></div>
  </section>

  <section class="card card--back" aria-label="Back of card – membership form">
    <div class="brand-mark"><span class="brand-mark__dot"></span><span class="brand-mark__name">Lighting<br>the Path</span></div>
    <p class="tagline">Computer Training for Educators</p>

    <form class="form-panel">
      <p class="form-panel__intro">To claim your <em>FREE membership</em> with Lighting the Path, simply fill out this form.</p>
      <div class="field"><span class="field__label">Given Name:</span><span class="field__line"></span></div>
      <div class="field"><span class="field__label">Surname:</span><span class="field__line"></span></div>
      <div class="field"><span class="field__label">Address:</span><span class="field__line"></span></div>
      <div class="field"><span class="field__line"></span></div>
      <div class="field field--split"><span class="field__label">City:</span><span class="field__line"></span><span class="field__label">Postcode:</span><span class="field__line field__line--short"></span></div>
      <div class="field"><span class="field__label">Gender: <span class="checkbox"></span>Male&nbsp;&nbsp; <span class="checkbox"></span>Female</span><span class="field__spacer"></span><span class="field__label">Date of Birth: <span class="placeholder">DD</span> / <span class="placeholder">MM</span> / <span class="placeholder">YYYY</span></span></div>
      <div class="field"><span class="field__label">Phone:</span><span class="field__line"></span></div>
      <div class="field"><span class="field__label">Email:</span><span class="field__line"></span></div>
      <div class="field"><span class="field__label">Additional Comments:</span><span class="field__line"></span></div>
      <div class="field"><span class="field__line"></span></div>
      <div class="field"><span class="field__line"></span></div>
    </form>

    <div class="return-box">
      <p class="return-box__title">PLEASE POST OR RETURN THIS FORM TO</p>
      <p class="return-box__address">ICT PD Membership, Lighting the Path<br>7 Kowhaiwai Terrace, Kelmore 4736</p>
    </div>
  </section>

</body>
</html>
```